Velimko AdAgency Presentation

We need ppt design for an ad agency re-branding, agency is based in Moscow, Russia. Our specifics is brand audit, consulting and strategy in web and offline.
We decided to do re-branding because our current agency does not answer the purpose and we need a kind of "second breath".
The idea of re-branding appeared because of many changes that happened in company: new clients, new projects level, new team.
So we'd like to promote company of changes and design should show this spirit as possible.
You may use info in attached pdf file (sorry for Russian language). Info is not so necessary, it will be replaced later.
Updates

Please use more colors than digital blue and grey!

Industry/Entity Type

Ad Agency

Requirements
Must have
• Logo is attached. Please choose one.

Ppt project should include:
- Front and last page design
- Heading and list design
- Page-separator design
- Diagram design
- Pics appearance

```html
<!DOCTYPE html>
<html lang="en">
<head>
<meta charset="utf-8">
<title>Velimko — Presentation Slides</title>
<link rel="stylesheet" href="https://fonts.googleapis.com/css2?family=Roboto:wght@300;400;500&family=Roboto+Condensed:wght@400;700&display=swap">
<style>
:root{
  --board:#232323;
  --slide-top:#e4e6e8;
  --slide-bottom:#eef0f1;
  --footer:#f8f8f6;
  --ink:#1f1f1f;
  --ink-soft:#444;
  --ink-muted:#777;
  --accent:#1aa6e4;
  --rule:#3a3a3a;
  --white:#ffffff;
}
*{margin:0;padding:0;box-sizing:border-box}
html,body{width:1200px;height:1200px;overflow:hidden;background:var(--board)}
body{position:relative;font-family:'Roboto',sans-serif;color:var(--ink)}

.slide{position:absolute;left:240px;width:720px;height:450px;
  background:radial-gradient(ellipse at 50% 40%,var(--slide-bottom),var(--slide-top));overflow:hidden}
.slide--project{top:58px}
.slide--content{top:570px}

.slide__divider{position:absolute;left:348px;top:100px;width:3px;height:270px;
  background:linear-gradient(to bottom,rgba(0,0,0,0),rgba(0,0,0,.07),rgba(0,0,0,0))}

.visual{position:absolute;border-radius:4px}
.visual--site{left:44px;top:124px;width:294px;height:154px;
  background:linear-gradient(160deg,#f1f0e4,#d9d6c6 55%,#b9b9b9)}
.visual--print{left:60px;top:158px;width:276px;height:168px;
  background:linear-gradient(150deg,#2b4f75,#4aa7d8 40%,#e8e4dc 70%,#b5412f)}

.tag{position:absolute;left:93px;top:52px;width:82px;height:92px;padding:5px 3px 0 5px;background:var(--accent);
  color:var(--white);font-family:'Roboto Condensed',sans-serif;font-weight:700;line-height:.96;text-transform:uppercase}
.tag__line{display:block;white-space:nowrap;overflow:hidden;letter-spacing:-.1px}
.tag__pointer{position:absolute;left:9px;bottom:-13px;width:0;height:0;
  border-right:13px solid transparent;border-top:13px solid var(--accent)}

.copy{position:absolute;left:382px;width:290px}
.slide--project .copy{top:126px}
.slide--content .copy{top:111px}
.copy__heading{font-family:'Roboto Condensed',sans-serif;font-weight:700;font-size:16.5px;color:var(--ink);text-transform:uppercase}
.copy__lead{font-size:13px;color:var(--ink-soft);line-height:16.5px;margin-top:8px}
.copy__link{color:var(--ink-muted)}
.copy__lead--small{font-size:10px;color:var(--ink);line-height:13.5px;margin-top:14px;width:260px}
.copy__body{font-size:7.6px;color:var(--ink-soft);line-height:13.6px;margin-top:36px;width:278px}
.slide--content .copy__body{margin-top:16px}
.copy__body + .copy__body{margin-top:13px}

.slide__footer{position:absolute;left:0;bottom:0;width:720px;height:55px;background:var(--footer);
  border-bottom:3px solid var(--accent);box-shadow:0 -1px 4px rgba(0,0,0,.04)}
.brand-mini{position:absolute;left:52px;top:8px;width:50px;text-align:center}
.brand-mini__square{display:block;width:20px;height:20px;margin:0 auto 3px;background:#555}
.brand-mini__name{font-size:8.5px;color:#555}
.footer__sep{position:absolute;top:14px;height:26px;border-left:1px dashed #c8c8c8}
.footer__sep--left{left:117px}
.footer__sep--right{left:572px}
.footer__title{position:absolute;left:146px;top:14px}
.footer__label{font-size:7px;color:var(--ink-muted)}
.footer__text{font-size:14px;color:var(--ink-soft);margin-top:1px}
.pager{position:absolute;left:588px;top:14px}
.pager__hint{font-size:5px;color:#666;letter-spacing:.1px;text-transform:uppercase}
.pager__hint b{color:var(--ink)}
.pager__row{display:flex;align-items:center;gap:8px;margin-top:6px}
.pager__btn{width:16px;height:16px;display:block}
.pager__count{font-size:10px;color:var(--ink-soft)}
.pager__count em{font-style:normal;color:#999}

.board-rule{position:absolute;left:38px;top:1068px;width:1108px;border-top:1px solid var(--rule)}
.board-brand{position:absolute;left:100px;top:1085px;width:92px;text-align:center}
.board-brand__square{display:block;width:52px;height:52px;margin:0 auto 8px;border:3px solid #e8e8e8;border-radius:3px}
.board-brand__name{font-size:22px;font-weight:300;color:#e8e8e8}
.board-caption{position:absolute;left:728px;top:1112px;font-size:19px;color:var(--white);letter-spacing:.1px;white-space:nowrap}
</style>
</head>
<body>

<section class="slide slide--project">
  <div class="visual visual--site" role="img" aria-label="Website pages of the textile company fanned out around a desktop monitor"></div>
  <div class="slide__divider"></div>
  <div class="copy">
    <h2 class="copy__heading">Project</h2>
    <p class="copy__lead">Subsite textile company Lintera<br><span class="copy__link">http://lintera-tex.ru/</span></p>
    <p class="copy__body">The main feature is the installation of management system Corvex, which gave the ability to synchronize with the site program Ledgr. We have also developed an advertising banner on the home page</p>
  </div>
  <footer class="slide__footer">
    <div class="brand-mini"><span class="brand-mini__square"></span><span class="brand-mini__name">Velimko</span></div>
    <span class="footer__sep footer__sep--left"></span>
    <div class="footer__title"><p class="footer__label">Slide title</p><p class="footer__text">Subsite textile company Lintera</p></div>
    <span class="footer__sep footer__sep--right"></span>
    <div class="pager">
      <p class="pager__hint">We are curretly <b>here</b></p>
      <div class="pager__row">
        <svg class="pager__btn" viewBox="0 0 16 16"><circle cx="8" cy="8" r="8" fill="#1aa6e4"/><path d="M9.5 4.5 6 8l3.5 3.5" stroke="#fff" stroke-width="1" fill="none"/></svg>
        <span class="pager__count">3 <em>Of 8</em></span>
        <svg class="pager__btn" viewBox="0 0 16 16"><circle cx="8" cy="8" r="8" fill="#1aa6e4"/><path d="M6.5 4.5 10 8l-3.5 3.5" stroke="#fff" stroke-width="1" fill="none"/></svg>
      </div>
    </div>
  </footer>
</section>

<section class="slide slide--content">
  <div class="tag">
    <span class="tag__line" style="font-size:8.6px">Web development</span>
    <span class="tag__line" style="font-size:9.4px">Annual report</span>
    <span class="tag__line" style="font-size:13.6px">Marketing</span>
    <span class="tag__line" style="font-size:8.6px">Material design</span>
    <span class="tag__line" style="font-size:9.2px">Merchandising</span>
    <span class="tag__line" style="font-size:8.8px">Company profile</span>
    <span class="tag__line" style="font-size:7.4px">Strategic planning</span>
    <span class="tag__line" style="font-size:12.6px">Production</span>
    <span class="tag__pointer"></span>
  </div>
  <div class="visual visual--print" role="img" aria-label="Printed magazines, brochures and menus spread over an open laptop"></div>
  <div class="slide__divider"></div>
  <div class="copy">
    <h2 class="copy__heading">Heading title write here</h2>
    <p class="copy__lead copy__lead--small">Completely synergize resource sucking relationships via premier niche markets.</p>
    <p class="copy__body">Collaboratively administrate empowered markets via plug-and-play networks. Dynamically procrastinate B2C users after installed base benefits. Dramatically visualize customer directed convergence without revolutionary ROI. Efficiently unleash cross-media information without cross-media value. Quickly maximize timely deliverables for real-time schemas. Dramatically maintain clicks-and-mortar solutions without functional solutions.</p>
    <p class="copy__body">Completely synergize resource sucking relationships via premier niche markets. Professionally cultivate one-to-one customer service with robust ideas. Dynamically innovate resource-leveling customer service for state of the art customer service.</p>
  </div>
  <footer class="slide__footer">
    <div class="brand-mini"><span class="brand-mini__square"></span><span class="brand-mini__name">Velimko</span></div>
    <span class="footer__sep footer__sep--left"></span>
    <div class="footer__title"><p class="footer__label">Slide title</p><p class="footer__text">CONTENT GOES HERE</p></div>
    <span class="footer__sep footer__sep--right"></span>
    <div class="pager">
      <p class="pager__hint">We are curretly <b>here</b></p>
      <div class="pager__row">
        <svg class="pager__btn" viewBox="0 0 16 16"><circle cx="8" cy="8" r="8" fill="#1aa6e4"/><path d="M9.5 4.5 6 8l3.5 3.5" stroke="#fff" stroke-width="1" fill="none"/></svg>
        <span class="pager__count">2 <em>Of 8</em></span>
        <svg class="pager__btn" viewBox="0 0 16 16"><circle cx="8" cy="8" r="8" fill="#1aa6e4"/><path d="M6.5 4.5 10 8l-3.5 3.5" stroke="#fff" stroke-width="1" fill="none"/></svg>
      </div>
    </div>
  </footer>
</section>

<div class="board-rule"></div>
<div class="board-brand"><span class="board-brand__square"></span><span class="board-brand__name">Velimko</span></div>
<p class="board-caption">POWER POINT PRESENTATION</p>

</body>
</html>
```